Design for Card Attached to Clothes

We sell rhythmic gymnastics apparel and are looking for someone create a card that will be attached to the products. You can see an example of the exact type of apparel in the files, as well as the current card that is attached to it. The design should have space on the top back for the sticker that has UPC and SKU information, as shown in the image attached.
- We would like the front to have our logo
- We would like the image of the girls added on the back
- Would be cool to see the gradient change to the white space on the back where the sticker will go but not required.
-The final card size is 10cm by 6cm, Their should be 2mm loss accounted for cutting the cards within the design. (meaning the design needs to be bigger than 10cm by 6cm to account for printing and cut)
- And the hole size that is at the top center is 3mm in diameter
- Name should be under logo
Access all logo files here https://files.plomvarek.net/share/folders/7Kq2TzWm9RbXa4LpYc8NdVe3Hs5JfGu1?view=open
- Front will have logo
- Back will have image of girls and some creative design that you will create.
Females
Rhythmic Gymnastics

```html
<!DOCTYPE html>
<html lang="en">
<head>
<meta charset="utf-8">
<title>Velorae Hang Tag – Front and Back</title>
<link rel="stylesheet" href="https://fonts.googleapis.com/css2?family=Lexend:wght@400&display=swap">
<style>
  :root {
    --backdrop: #c6c4c5;
    --card-white: #ffffff;
    --brand-magenta: #e2006b;
    --pink-soft: #f6d3df;
    --pink-mid: #e8507f;
    --pink-deep: #c25a9c;
    --hole: #c6c4c5;
    --photo-top: rgba(176, 62, 110, 0.35);
    --photo-mid: rgba(120, 40, 80, 0.55);
    --photo-base: rgba(58, 34, 46, 0.8);
  }
  * { box-sizing: border-box; margin: 0; padding: 0; }
  html, body {
    width: 1200px;
    height: 987px;
    overflow: hidden;
    background: var(--backdrop);
  }
  .sheet {
    position: relative;
    width: 1200px;
    height: 987px;
  }
  .tag {
    position: absolute;
    overflow: hidden;
  }
  .tag-front {
    left: 89px;
    top: 92px;
    width: 482px;
    height: 803px;
    background: var(--card-white);
  }
  .tag-back {
    left: 633px;
    top: 91px;
    width: 477px;
    height: 804px;
    background: linear-gradient(
      to bottom,
      #ffffff 0%,
      #fbeef2 18%,
      var(--pink-soft) 40%,
      #ee8fac 55%,
      var(--pink-mid) 66%,
      #dc5389 82%,
      var(--pink-deep) 100%
    );
  }
  .hang-hole {
    position: absolute;
    top: 25px;
    width: 24px;
    height: 24px;
    border-radius: 50%;
    background: var(--hole);
  }
  .tag-front .hang-hole { left: 222px; }
  .tag-back .hang-hole { left: 225px; }

  .brand-dot {
    position: absolute;
    left: 137px;
    top: 366px;
    width: 200px;
    height: 200px;
    border-radius: 50%;
    background: var(--brand-magenta);
  }
  .brand-name {
    position: absolute;
    left: 0;
    width: 100%;
    top: 654px;
    text-align: center;
    font-family: "Lexend", sans-serif;
    font-weight: 400;
    font-size: 92px;
    letter-spacing: -2px;
    line-height: 1;
    color: var(--brand-magenta);
  }

  .gymnasts-photo {
    position: absolute;
    left: 24px;
    top: 388px;
    width: 424px;
    height: 347px;
    border-radius: 28px;
    background: linear-gradient(
      to bottom,
      var(--photo-top) 0%,
      var(--photo-mid) 55%,
      var(--photo-base) 100%
    );
  }
</style>
</head>
<body>
  <main class="sheet">
    <section class="tag tag-front" aria-label="Tag front">
      <span class="hang-hole"></span>
      <span class="brand-dot"></span>
      <p class="brand-name">Velorae</p>
    </section>

    <section class="tag tag-back" aria-label="Tag back">
      <span class="hang-hole"></span>
      <div class="gymnasts-photo" role="img" aria-label="Photo of two young rhythmic gymnasts in black leotards and leggings, kneeling in a backbend with one arm raised"></div>
    </section>
  </main>
</body>
</html>
```